Business Card Design

Quorvel Software Limited develops and sells venue and event management software called Quorvel Stagehand, which is available in the cloud or on-premise. The company was established in 1986. Most of our customers are performing arts venues, museums and festivals. Our existing design is a bit dull. We need to convey that we are both innovative and reliable.
Not all our people show their mobile phone numbers on their cards, so the design needs to work land line and mobile or land line only.

Industry/Entity Type

Software

Contact Information for Business Card

Helen Brackwood
Director
Quorvel Software Limited
42B Millbank Lane, Epsom, Surrey, KT19 3DW
Telephone: +44 (0)1372 904213
Mobile: +44 (0)7700 900562
Email: hbrackwood@quorvel.example
Web: www.quorvel.example

```html
<!DOCTYPE html>
<html lang="en">
<head>
<meta charset="utf-8">
<title>Quorvel Software Limited – Business Card</title>
<link rel="stylesheet" href="https://fonts.googleapis.com/css2?family=Lato:wght@400;700;900&display=swap">
<style>
  :root {
    --backdrop: #dcdee1;
    --card: #ffffff;
    --navy: #1b4a78;
    --blue: #1f6aa5;
    --blue-dark: #164f80;
    --ink: #1c3452;
    --grey: #8b8d90;
  }
  * { box-sizing: border-box; margin: 0; padding: 0; }
  html, body { width: 1200px; height: 926px; overflow: hidden; }
  body {
    background: var(--backdrop);
    font-family: "Lato", sans-serif;
    display: flex;
    flex-direction: column;
    align-items: center;
    justify-content: center;
    gap: 44px;
  }
  .card {
    position: relative;
    width: 560px;
    height: 362px;
    background: var(--card);
    box-shadow: 0 6px 18px rgba(0,0,0,0.18);
    overflow: hidden;
  }
  .brand {
    display: flex;
    align-items: center;
    gap: 14px;
    color: var(--navy);
    font-weight: 900;
    letter-spacing: 0.04em;
  }
  .brand-square {
    width: 38px;
    height: 38px;
    background: var(--navy);
  }
  .brand-name { font-size: 34px; line-height: 1; }

  /* Front */
  .card-front {
    display: flex;
    flex-direction: column;
    align-items: center;
    justify-content: center;
    gap: 26px;
  }
  .card-front .brand-name { font-size: 40px; }
  .card-front .brand-square { width: 46px; height: 46px; }
  .front-web {
    color: var(--navy);
    font-size: 15px;
    letter-spacing: 0.42em;
  }

  /* Back */
  .card-back .brand {
    position: absolute;
    left: 36px;
    top: 36px;
  }
  .company {
    position: absolute;
    left: 36px;
    top: 138px;
    color: var(--blue);
  }
  .company-name { font-size: 24px; font-weight: 700; }
  .company-address { font-size: 15px; margin-top: 2px; }
  .contacts {
    position: absolute;
    left: 36px;
    top: 206px;
    list-style: none;
    color: var(--ink);
    font-size: 14.5px;
    line-height: 1.32;
  }
  .contacts .label { font-weight: 700; }
  .person {
    position: absolute;
    right: 34px;
    top: 232px;
    text-align: right;
    padding-right: 14px;
  }
  .person::after {
    content: "";
    position: absolute;
    right: 0;
    top: 2px;
    width: 8px;
    height: 48px;
    background: var(--blue);
  }
  .person-name {
    color: var(--blue);
    font-size: 22px;
    font-weight: 400;
    text-transform: uppercase;
    letter-spacing: 0.01em;
  }
  .person-name strong { font-weight: 700; }
  .person-role {
    color: var(--grey);
    font-size: 17px;
    letter-spacing: 0.06em;
    text-transform: uppercase;
  }
  .footer-band {
    position: absolute;
    left: 0;
    right: 0;
    bottom: 0;
    height: 14px;
    display: flex;
    gap: 3px;
  }
  .footer-band .band-left { flex: 0 0 62%; background: var(--blue-dark); }
  .footer-band .band-right { flex: 1; background: var(--blue); }
</style>
</head>
<body>
  <section class="card card-front" aria-label="Card front">
    <div class="brand">
      <span class="brand-square"></span>
      <span class="brand-name">QUORVEL</span>
    </div>
    <p class="front-web">www.quorvel.example</p>
  </section>

  <section class="card card-back" aria-label="Card back">
    <div class="brand">
      <span class="brand-square"></span>
      <span class="brand-name">QUORVEL</span>
    </div>
    <div class="company">
      <p class="company-name">Quorvel Software Limited</p>
      <p class="company-address">42B Millbank Lane, Epsom, Surrey, KT19 3DW</p>
    </div>
    <ul class="contacts">
      <li><span class="label">telephone:</span> +44 (0)1372 904213</li>
      <li><span class="label">mobile:</span> +44 (0)7700 900562</li>
      <li><span class="label">email:</span> hbrackwood@quorvel.example</li>
      <li><span class="label">web:</span> www.quorvel.example</li>
    </ul>
    <div class="person">
      <p class="person-name">Helen <strong>Brackwood</strong></p>
      <p class="person-role">Director</p>
    </div>
    <div class="footer-band">
      <span class="band-left"></span>
      <span class="band-right"></span>
    </div>
  </section>
</body>
</html>
```